Body therapist needs a business card

I need a card for my business which is teaching trainings in body therapy, the company is called Wellacombe Educational Group. I teach to massage therapists around Australia, South East Asia and the USA. I am attaching my logo which will guide you as to what colours I would like to have you consider. Please consult my website to find out more about what I do. www.kinetrova.com.au

My name is Gareth Wellacombe. My phone number is (03) 9157 2618 or 0412573086. email is info@kinetrova.com.au

```html
<!DOCTYPE html>
<html lang="en">
<head>
<meta charset="utf-8">
<title>Wellacombe Educational Group – Business Card</title>
<link href="https://fonts.googleapis.com/css2?family=Open+Sans:wght@400&family=Work+Sans:wght@400;600&display=swap" rel="stylesheet">
<style>
  :root {
    --backdrop: #1b1b1b;
    --card: #262626;
    --card-edge: #2e2e2e;
    --ink: #f2f2f2;
    --lime: #cddc0c;
  }
  * { box-sizing: border-box; margin: 0; padding: 0; }
  html, body { width: 1200px; height: 900px; overflow: hidden; }
  body {
    background: var(--backdrop);
    position: relative;
    font-family: "Work Sans", Arial, sans-serif;
    color: var(--ink);
  }
  .card {
    position: absolute;
    left: 250px;
    width: 700px;
    height: 400px;
    background: linear-gradient(135deg, var(--card) 0%, var(--card-edge) 100%);
    box-shadow: 0 14px 30px rgba(0,0,0,.55);
  }
  .card--front { top: 30px; }
  .card--back { top: 470px; }

  .brand {
    position: absolute;
    left: 170px;
    top: 150px;
    display: flex;
    align-items: center;
    gap: 22px;
  }
  .brand__dot {
    width: 54px; height: 54px;
    border-radius: 50%;
    background: var(--lime);
    flex: none;
  }
  .brand__name {
    font-family: "Open Sans", Arial, sans-serif;
    font-weight: 400;
    color: var(--ink);
    line-height: 1.05;
  }
  .brand__word { display: block; font-size: 44px; letter-spacing: 1px; }
  .brand__sub { display: block; font-size: 19px; margin-top: 4px; }

  .identity {
    position: absolute;
    right: 378px;
    top: 150px;
    text-align: right;
  }
  .identity__name {
    color: var(--lime);
    font-weight: 600;
    font-size: 26px;
    letter-spacing: .3px;
  }
  .identity__role { font-size: 19px; letter-spacing: 1px; margin-top: 4px; }
  .identity__address { font-size: 17px; letter-spacing: 1px; line-height: 1.45; margin-top: 4px; }

  .divider {
    position: absolute;
    left: 345px;
    top: 205px;
    width: 2px;
    height: 92px;
    background: var(--lime);
  }

  .contacts {
    position: absolute;
    left: 380px;
    top: 212px;
    list-style: none;
    font-size: 18px;
    letter-spacing: 1.2px;
    line-height: 1.5;
  }
  .contacts li { display: flex; align-items: center; gap: 10px; }
  .contacts svg { width: 13px; height: 13px; flex: none; }
</style>
</head>
<body>
  <section class="card card--front">
    <div class="brand">
      <span class="brand__dot"></span>
      <span class="brand__name">
        <span class="brand__word">Wellacombe</span>
        <span class="brand__sub">Educational Group</span>
      </span>
    </div>
  </section>

  <section class="card card--back">
    <div class="identity">
      <p class="identity__name">Gareth Wellacombe</p>
      <p class="identity__role">Director</p>
      <p class="identity__address">P.O. Box 2784 Ashvale North<br>Victoria, 3149 Australia</p>
    </div>
    <span class="divider"></span>
    <ul class="contacts">
      <li>
        <svg viewBox="0 0 16 16" aria-hidden="true"><path d="M4 1l3 3-2 2c1 2 3 4 5 5l2-2 3 3-2 2C7 14 2 9 2 3z" fill="var(--lime)"/></svg>
        03 9157 2618
      </li>
      <li>
        <svg viewBox="0 0 16 16" aria-hidden="true"><rect x="4" y="1" width="8" height="14" rx="1.5" fill="none" stroke="var(--lime)" stroke-width="1.6"/><circle cx="8" cy="12.5" r="1" fill="var(--lime)"/></svg>
        0412573086
      </li>
      <li>
        <svg viewBox="0 0 16 16" aria-hidden="true"><rect x="1.5" y="3.5" width="13" height="9" fill="none" stroke="var(--lime)" stroke-width="1.4"/><path d="M1.5 3.5L8 9l6.5-5.5" fill="none" stroke="var(--lime)" stroke-width="1.4"/></svg>
        info@kinetrova.com.au
      </li>
      <li>
        <svg viewBox="0 0 16 16" aria-hidden="true"><circle cx="8" cy="8" r="6.5" fill="none" stroke="var(--lime)" stroke-width="1.3"/><ellipse cx="8" cy="8" rx="2.8" ry="6.5" fill="none" stroke="var(--lime)" stroke-width="1.1"/><path d="M1.5 8h13" stroke="var(--lime)" stroke-width="1.1"/></svg>
        www.kinetrova.com.au
      </li>
    </ul>
  </section>
</body>
</html>
```